pop up booking component and calendar re-design

we have a calander view where a parent cant reserve a day
you can click on please redesign the calander / voucher and pop up.

the dropdowns in pop up can be buttons
the dots on the calander indicate if there is space or not

when booking a day you can select a voucher

we used MELO as inspiration, you are welcome to look at it as well.. screenshots attached

please ask questions if you have any

```html
<!DOCTYPE html>
<html lang="en">
<head>
<meta charset="utf-8">
<title>Book Day – Calendar</title>
<link rel="stylesheet" href="https://fonts.googleapis.com/css2?family=Inter:wght@400;500;600;700&display=swap">
<style>
  :root {
    --yellow: #ffd60a;
    --orange: #ffa000;
    --accent: #f5a10a;
    --overlay: #8d8d8d;
    --overlay-dark: #6f6f6f;
    --muted-on-overlay: #6a6a6a;
    --white: #ffffff;
    --ink: #111111;
    --grey-text: #a9a9a9;
    --line: #d6d6d6;
    --tab-idle: #c4c4c4;
    --toggle: #c3c5c9;
    --blue: #4a8bef;
  }
  * { box-sizing: border-box; margin: 0; padding: 0; }
  html, body { width: 1200px; height: 2597px; overflow: hidden; }
  body { position: relative; background: var(--overlay); font-family: "Inter", sans-serif; color: var(--ink); }
  .abs { position: absolute; }

  .header { left: 0; top: 0; width: 1200px; height: 454px; background: linear-gradient(180deg, var(--yellow) 0%, var(--orange) 100%); }
  .status-time { left: 69px; top: 48px; font-size: 44px; font-weight: 600; display: flex; align-items: center; gap: 6px; }
  .status-icons { right: 60px; top: 52px; display: flex; gap: 16px; align-items: center; }
  .nav-arrow { top: 180px; }
  .month-pill { left: 185px; top: 161px; width: 831px; height: 100px; border-radius: 50px; background: var(--white); box-shadow: 0 6px 14px rgba(0,0,0,.12); display: flex; align-items: center; justify-content: center; font-size: 41px; }
  .month-pill svg { position: absolute; right: 36px; top: 29px; }
  .view-tabs { top: 335px; left: 0; width: 1200px; font-size: 41px; color: rgba(255,255,255,.75); }
  .view-tabs span { position: absolute; transform: translateX(-50%); white-space: nowrap; }
  .view-tabs .active { color: var(--ink); font-weight: 700; }

  .back-card { left: 104px; top: 2060px; width: 994px; height: 42px; background: #858585; border-radius: 8px; }
  .modal { left: 104px; top: 518px; width: 994px; height: 1562px; background: var(--white); border-radius: 7px; }
  .modal-tab { top: 40px; font-size: 41px; transform: translateX(-50%); white-space: nowrap; }
  .modal-tab.active { left: 249px; font-weight: 700; }
  .modal-tab.idle { left: 746px; color: var(--tab-idle); }
  .tab-bar { top: 134px; height: 6px; }
  .availability { top: 196px; left: 0; width: 994px; text-align: center; font-size: 24px; color: #333; }
  .divider { left: 41px; top: 278px; width: 910px; height: 2px; background: var(--line); }
  .field-label { top: 312px; font-size: 35px; color: #333; letter-spacing: .5px; }
  .field-label b { color: var(--accent); font-weight: 400; }
  .field-box { top: 381px; height: 111px; width: 278px; border-radius: 14px; background: var(--white); box-shadow: 0 3px 10px rgba(0,0,0,.16); display: flex; align-items: center; padding-left: 31px; font-size: 26px; }
  .field-box svg { position: absolute; right: 30px; top: 48px; }
  .toggle { left: 738px; top: 398px; width: 151px; height: 80px; border-radius: 40px; background: var(--toggle); }
  .toggle::after { content: ""; position: absolute; left: 13px; top: 12px; width: 56px; height: 56px; border-radius: 50%; background: var(--white); }
  .option { height: 107px; border: 2.5px solid var(--accent); border-radius: 14px; color: var(--accent); font-weight: 700; font-size: 26px; display: flex; align-items: center; padding-left: 30px; }
  .cta { left: 41px; width: 910px; height: 152px; border-radius: 14px; background: linear-gradient(180deg, var(--yellow) 0%, var(--orange) 100%); color: var(--white); font-weight: 700; font-size: 50px; display: flex; align-items: center; justify-content: center; }
  .summary { left: 41px; top: 1027px; width: 910px; height: 301px; border: 2px solid #e3e3e3; border-radius: 12px; }
  .summary-row { left: 0; width: 906px; display: flex; align-items: center; justify-content: space-between; padding: 0 48px 0 29px; font-size: 26px; color: var(--grey-text); }
  .summary-row.total { color: var(--ink); font-weight: 700; }
  .row-line { left: 0; width: 906px; height: 2px; background: #d9d9d9; }
  .apply { width: 111px; height: 42px; border-radius: 21px; background: var(--blue); color: var(--white); font-size: 21px; display: flex; align-items: center; justify-content: center; }

  .actions { top: 2240px; font-size: 49px; color: var(--muted-on-overlay); transform: translateX(-50%); white-space: nowrap; }
  .action-sep { top: 2225px; width: 2px; height: 101px; background: var(--muted-on-overlay); }
  .promo-btn { left: 104px; top: 2384px; width: 994px; height: 152px; border-radius: 10px; background: var(--overlay-dark); border: 2px solid #666; color: #8f8f8f; font-weight: 700; font-size: 52px; display: flex; align-items: center; justify-content: center; }
</style>
</head>
<body>
  <header class="header abs">
    <div class="status-time abs">12:01
      <svg width="32" height="32" viewBox="0 0 24 24"><path d="M21 3 3 11l8 2 2 8z" fill="#111"/></svg>
    </div>
    <div class="status-icons abs">
      <svg width="56" height="34" viewBox="0 0 56 34"><rect x="0" y="22" width="9" height="12" rx="2" fill="#111"/><rect x="14" y="15" width="9" height="19" rx="2" fill="#111"/><rect x="28" y="8" width="9" height="26" rx="2" fill="#111"/><rect x="42" y="0" width="9" height="34" rx="2" fill="#111" opacity=".35"/></svg>
      <svg width="48" height="36" viewBox="0 0 48 36"><path d="M24 34 31 26a10 10 0 0 0-14 0z" fill="#111"/><path d="M9 18a21 21 0 0 1 30 0l-4 4a15 15 0 0 0-22 0z" fill="#111"/><path d="M2 11a31 31 0 0 1 44 0l-4 4a25 25 0 0 0-36 0z" fill="#111"/></svg>
      <svg width="78" height="38" viewBox="0 0 78 38"><rect x="2" y="2" width="66" height="34" rx="9" fill="none" stroke="#111" stroke-width="3" opacity=".6"/><rect x="7" y="7" width="34" height="24" rx="5" fill="#f5a623"/><rect x="71" y="13" width="5" height="12" rx="2" fill="#111" opacity=".6"/><path d="M40 5 28 21h9l-3 12 12-16h-9z" fill="#111"/></svg>
    </div>
    <svg class="nav-arrow abs" style="left:72px" width="40" height="64" viewBox="0 0 40 64"><path d="M34 4 6 32l28 28" fill="none" stroke="#111" stroke-width="4"/></svg>
    <svg class="nav-arrow abs" style="left:1090px" width="40" height="64" viewBox="0 0 40 64"><path d="M6 4l28 28L6 60" fill="none" stroke="#555" stroke-width="4"/></svg>
    <div class="month-pill abs">Novmeber 2019
      <svg width="44" height="44" viewBox="0 0 44 44"><g fill="none" stroke="#777" stroke-width="2.5"><circle cx="10" cy="10" r="8"/><circle cx="34" cy="10" r="8"/><circle cx="10" cy="34" r="8"/><circle cx="34" cy="34" r="8"/></g></svg>
    </div>
    <nav class="view-tabs abs">
      <span style="left:358px">Today</span>
      <span class="active" style="left:514px">Day</span>
      <span style="left:667px">Week</span>
      <span style="left:840px">Month</span>
    </nav>
  </header>

  <div class="back-card abs"></div>

  <section class="modal abs">
    <div class="modal-tab active abs">Book Day</div>
    <div class="modal-tab idle abs">Vouchers</div>
    <div class="tab-bar abs" style="left:0;width:495px;background:var(--orange)"></div>
    <div class="tab-bar abs" style="left:495px;width:499px;background:#c2c2c2"></div>

    <p class="availability abs">Availability -&nbsp;&nbsp;&nbsp;1m/1a left 24-10-2019</p>
    <div class="divider abs"></div>

    <div class="field-label abs" style="left:64px">LOCATIONS<b>*</b></div>
    <div class="field-label abs" style="left:405px">GROUPS<b>*</b></div>
    <div class="field-label abs" style="left:812px;transform:translateX(-50%)">BSO</div>

    <div class="field-box abs" style="left:41px">RBW</div>
    <div class="field-box abs" style="left:357px">3-Penguins
      <svg width="18" height="14" viewBox="0 0 18 14"><path d="M1 1h16L9 13z" fill="#111"/></svg>
    </div>
    <div class="toggle abs"></div>

    <div class="option abs" style="left:41px;top:531px;width:278px">FULL</div>
    <div class="option abs" style="left:358px;top:531px;width:277px">AM</div>
    <div class="option abs" style="left:674px;top:531px;width:277px">PM</div>
    <div class="option abs" style="left:41px;top:680px;width:433px">FLEX</div>
    <div class="option abs" style="left:518px;top:680px;width:433px">TRY</div>

    <div class="cta abs" style="top:833px">Restart</div>

    <div class="summary abs">
      <div class="summary-row abs" style="top:0;height:99px"><span>Price</span><span>€ 98.23</span></div>
      <div class="row-line abs" style="top:99px"></div>
      <div class="summary-row abs" style="top:101px;height:95px"><span>Voucher</span><span class="apply">Apply</span></div>
      <div class="row-line abs" style="top:196px"></div>
      <div class="summary-row total abs" style="top:198px;height:99px"><span>Total</span><span>€ 98.23</span></div>
    </div>

    <div class="cta abs" style="top:1362px">Confirm</div>
  </section>

  <div class="actions abs" style="left:265px">Not Coming</div>
  <div class="action-sep abs" style="left:454px"></div>
  <div class="actions abs" style="left:620px">Unselect</div>
  <div class="action-sep abs" style="left:787px"></div>
  <div class="actions abs" style="left:933px">Cancel</div>

  <div class="promo-btn abs">Vouchers / Promotions</div>
</body>
</html>
```